TrellanVita Website - Biologics storage and handling

I would like a beginning design on a website for TrellanVita:

A Boston-based company dedicated to sourcing, storing, and supplying biologic materials of all kinds to the life sciences and scientific markets. From starting reagents, to basic and intermediate materials, to final synthesized and engineered products, we provide value throughout the biologics supply chain. TrellanVita provides backup, overflow, emergency, and stocking storage solutions to companies on a temporary or permanent basis. Life sciences companies can take advantage of the fact that the company is located in the middle of the Boston/Cambridge biotechnology corridor in order to have quick and efficient access to their cold chain materials. Out of state companies can leverage TrellanVita’s location for efficient distribution of materials to partner and client organizations. We also provide other value added services to organizations that do not have the local manpower, such as sourcing, supply, and distribution of materials.

The design should be mostly a white background with clean, linear, geometric colors added in according to the blue and orange color scheme represented in the corporate logo attached.

The website needs to communicate reliable service and provide the concept of a company dedicated to handling and providing client biological samples in a secure and efficient manner.

Some local competitors are:
1. Korbel BioWorks: www.korbelbw.example
2. TrellanVita: www.labvault-store.example

From a design perspective, I like the Halvenor Thera website:

www.halvenorthera.example

Target Market(s)

Life sciences companies and other organizations

Industry/Entity Type

Biotechnology

Coding

Coded - Design and coding required

Number of Pages Required

5+ page

Font styles to use
Sans Serif

Colors
3176b5
0455a3
f37122

Requirements
Must have
• Tabs for pages:
About - Company information.
Platform - Inventory and sample management cloud platform; temperature profiling, logging, and reporting.
Services - Refrigeration and freezing services for biological samples, logistics services, sourcing services, courier services.
Updates - News, events, blog.
Login portal - Entry point for getting into platform. Maybe some freemium content here.
Nice to have
• Please be creative about website page sections, vibrant colors according to my established color scheme, and clean, linear, geometric shapes. I would like a white background with nice colors, clean lines and borders, and a very contemporary look. I want o
Should not have
• This is not a Business to Consumer business. This is a Business to Business enterprise. There should not be consumer oriented language. It is more about service and relationship management.

```html
<!DOCTYPE html>
<html lang="en">
<head>
<meta charset="utf-8">
<title>TrellanVita — Biological Materials</title>
<link href="https://fonts.googleapis.com/css2?family=Montserrat:wght@400;500;600;700&family=Open+Sans:wght@400;600;700&family=Noto+Serif:wght@400&family=Ubuntu:wght@700&display=swap" rel="stylesheet">
<style>
:root{
  --orange:#e8690b;
  --orange-bright:#f47a1c;
  --orange-deep:#ff5a1f;
  --blue:#0a78d8;
  --teal:#1f5a6c;
  --ink:#1d2530;
  --muted:#7d7d86;
  --soft:#f3f2f4;
  --footer:#24272f;
  --footer-deep:#1c1e25;
  --white:#ffffff;
}
*{margin:0;padding:0;box-sizing:border-box}
html,body{width:1200px;height:3182px;overflow:hidden;background:var(--white);font-family:"Montserrat",sans-serif;color:var(--ink)}
.page{position:relative;width:1200px;height:3182px}

/* header */
.site-header{position:absolute;left:0;top:0;width:1200px;height:160px;background:var(--white)}
.brand{position:absolute;left:0;width:1200px;top:72px;display:flex;justify-content:center;align-items:center;gap:12px}
.brand-mark{width:22px;height:22px;background:var(--teal)}
.brand-name{font-family:"Montserrat",sans-serif;font-weight:500;font-size:36px;color:var(--teal);letter-spacing:1px}
.main-nav{position:absolute;left:0;top:160px;width:1200px;height:35px;background:var(--orange);display:flex;justify-content:center;align-items:center;gap:18px}
.main-nav a{font-family:"Noto Serif",serif;font-size:12.5px;color:var(--white);text-decoration:none;white-space:nowrap}

/* hero */
.hero{position:absolute;left:0;top:195px;width:1200px;height:549px;background:linear-gradient(180deg,#8f9aa3 0%,#b7bec4 40%,#8b8a88 75%,#6c625c 100%)}
.hero-shade{position:absolute;inset:0;background:rgba(20,25,30,.25)}
.hero-title{position:absolute;top:245px;left:0;width:1200px;text-align:center;font-family:"Ubuntu",sans-serif;font-weight:700;font-size:70px;color:var(--white)}
.hero-text{position:absolute;top:348px;left:280px;width:640px;text-align:center;font-size:15.5px;line-height:19px;color:var(--white)}
.btn{display:inline-flex;align-items:center;justify-content:center;background:var(--orange-bright);color:var(--white);font-weight:600;font-size:11px;text-transform:uppercase}
.hero .btn{position:absolute;left:513px;top:444px;width:158px;height:36px}

/* services */
.services{position:absolute;left:0;top:744px;width:1200px;height:566px;background:var(--soft)}
.section-title{position:absolute;left:0;width:1200px;text-align:center;font-weight:700;font-size:31px;color:var(--ink)}
.section-tag{position:absolute;left:0;width:1200px;display:flex;justify-content:center;align-items:center;gap:8px;font-size:9px;font-weight:600;color:var(--teal)}
.section-tag::before,.section-tag::after{content:"";width:68px;height:1px;background:#555}
.tabs{position:absolute;left:224px;top:183px;width:739px;height:46px;background:var(--blue);display:flex;align-items:center;padding-left:46px;gap:36px}
.tabs span{font-size:12px;color:var(--white);position:relative}
.tabs .active::after{content:"";position:absolute;left:0;right:0;bottom:-8px;height:2px;background:var(--white)}
.service-photo{position:absolute;left:224px;top:258px;width:347px;height:251px;background:linear-gradient(135deg,#d7e8f2 0%,#6fb3d6 45%,#1f7fb0 100%)}
.service-heading{position:absolute;left:617px;top:252px;font-weight:700;font-size:22px;color:var(--ink)}
.service-text{position:absolute;left:617px;top:297px;width:346px;font-size:10px;line-height:15px;color:var(--muted)}
.service-text p+p{margin-top:14px}
.services .btn{position:absolute;left:614px;top:474px;width:103px;height:35px}

/* storage */
.storage{position:absolute;left:0;top:1310px;width:1200px;height:590px;background:var(--white)}
.storage-title{position:absolute;left:0;top:62px;width:1200px;text-align:center;font-weight:500;font-size:24px;line-height:30px;color:var(--teal)}
.storage-card{position:absolute;left:240px;top:167px;width:715px;height:335px;background:var(--white);box-shadow:0 2px 8px rgba(0,0,0,.12);padding:62px 30px 0;text-align:center;font-size:11px;line-height:18.7px;color:#555}
.storage-card p+p{margin-top:18.7px}

/* why */
.why{position:absolute;left:0;top:1900px;width:1200px;height:295px;background:linear-gradient(120deg,var(--orange-deep) 0%,#ff6a2c 50%,#ff7a3c 100%)}
.why-title{position:absolute;left:0;top:36px;width:1200px;text-align:center;font-weight:600;font-size:23px;color:var(--white)}
.why-item{position:absolute;top:162px;display:flex;align-items:center;gap:20px;color:#ffe4d6;font-size:19px;line-height:25px}
.why-item svg{flex:none}

/* news */
.news{position:absolute;left:0;top:2195px;width:1200px;height:667px;background:var(--white)}
.news-card{position:absolute;top:170px;width:231px;height:428px;border:1px solid #eee;background:var(--white)}
.news-photo{height:232px;position:relative}
.news-badge{position:absolute;left:18px;top:19px;background:var(--orange-bright);color:var(--white);font-size:8px;font-weight:700;padding:5px 8px}
.news-body{padding:20px 18px 0}
.news-meta{font-family:"Open Sans",sans-serif;font-size:9px;color:var(--muted)}
.news-title{font-family:"Open Sans",sans-serif;font-weight:700;font-size:13.5px;line-height:18px;color:var(--ink);margin-top:12px}
.news-text{font-family:"Open Sans",sans-serif;font-size:10.5px;line-height:16px;color:#8f8f98;margin-top:10px}
.news-more{font-family:"Open Sans",sans-serif;font-weight:600;font-size:10px;color:var(--ink);margin-top:13px}

/* footer */
.site-footer{position:absolute;left:0;top:2862px;width:1200px;height:283px;background:var(--footer)}
.footer-brand{position:absolute;left:229px;top:34px;font-weight:700;font-size:25px;color:var(--orange-bright)}
.footer-about{position:absolute;left:229px;top:76px;width:175px;font-size:10.5px;line-height:16.5px;color:#d9d9de}
.socials{position:absolute;left:229px;top:176px;display:flex;gap:12px}
.socials span{width:29px;height:29px;border-radius:50%;background:#3a3d46}
.footer-col{position:absolute;top:38px}
.footer-col h4{font-size:11.5px;font-weight:700;color:var(--white);letter-spacing:.5px}
.footer-links{margin-top:24px;list-style:none}
.footer-links li{font-size:9.5px;color:#d9d9de;margin-bottom:14px}
.footer-links li::before{content:"› ";}
.post{font-size:10.5px;line-height:16px;color:#d9d9de;width:171px}
.post-date{display:flex;gap:7px;align-items:center;margin-top:8px;font-size:10.5px}
.post-divider{width:171px;height:1px;background:#555;margin:8px 0 14px}
.subscribe-input{margin-top:14px;width:171px;height:31px;background:#363944;font-size:9px;color:#9a9aa3;padding:10px 13px}
.subscribe-btn{margin-top:10px;width:108px;height:33px}
.footer-bottom{position:absolute;left:0;top:3145px;width:1200px;height:37px;background:var(--footer-deep);text-align:center;font-size:8.5px;line-height:37px;color:#d9d9de}
.footer-bottom em{font-style:normal;color:var(--orange-bright)}
</style>
</head>
<body>
<div class="page">

<header class="site-header">
  <div class="brand"><span class="brand-mark"></span><span class="brand-name">TrellanVita</span></div>
</header>
<nav class="main-nav">
  <a>Home</a><a>About</a><a>Platform</a><a>Services</a><a>Biological Storage</a><a>Cold Chain Logistics</a><a>Updates</a><a>Contact</a><a>Login</a>
</nav>

<section class="hero" role="img" aria-label="Photo of a scientist working at a laboratory bench with glassware">
  <div class="hero-shade"></div>
  <h1 class="hero-title">Biological Materials</h1>
  <p class="hero-text">TrellanVita is dedicated to sourcing, storing, and supplying biologic materials of all kinds to the life sciences and scientific markets</p>
  <span class="btn">Know More</span>
</section>

<section class="services">
  <h2 class="section-title" style="top:68px">OUR SERVICES</h2>
  <div class="section-tag" style="top:110px">WORK AREA</div>
  <div class="tabs">
    <span class="active">Backup</span><span>Overflow</span><span>Emergency</span><span>Stocking Storage Solutions</span><span>ManPower</span><span>Resource</span>
  </div>
  <div class="service-photo" role="img" aria-label="Photo of a gloved hand pipetting into lab tubes beside a flask of blue liquid"></div>
  <h3 class="service-heading">Backup Process</h3>
  <div class="service-text">
    <p>Excepteur sint occaecat cupidatat non proident sunt in culpa qui officia desunt mollit anim id est laborum. sed ut per spiciatis unde omnis natus error vitae inventore veritatis quasi architebeatae vitae dicta sunt explicabo nemo enim ipsam voluptatem quia voluptassit.aspernatur aut odit aut fugit sed quia eos consequntur magni dolores eos qui ratione</p>
    <p>Sequi nesciunt neque porro qusquam est qui dolore ipsum quia dolor sit amet consecteturadipisc velit sed quia non numquam eius modi.</p>
  </div>
  <span class="btn">Read More</span>
</section>

<section class="storage">
  <h2 class="storage-title">Biological &amp; Pharmaceutical Storage Facilities<br>Services</h2>
  <div class="storage-card">
    <p>TrellanVita offers dedicated Pharmaceutical, Biological, and Consumer Products Sample Management Services in its fully cGMP compliant state of the art facilities. TrellanVita stores over 30,000,000 of our clients most precious and valuable samples in over 300 freezers and walk in rooms. Our state-of-the-art facilities are located throughout the U.S. We are currently expanding, and service the ever-increasing global market. We offer everything from cold chain delivery to cold storage in our Boston/Cambridge biotechnology corridor.</p>
    <p>Whether clients are storing 3 or 3,000,000 samples TrellanVita offers the same customer focused service, which allows clients unprecedented access and control of samples. With an integrated cold chain logistics fleet, TrellanVita is able to offer complete chain of custody and audit trail for each and every sample.</p>
    <p>TrellanVita is quickly establishing itself as a global leader in pharmaceutical and biological sample management and is dedicated to the specific needs of each individual customer/partner.</p>
  </div>
</section>

<section class="why">
  <h2 class="why-title">Why Chose Us?</h2>
  <div class="why-item" style="left:208px;top:158px"><svg width="20" height="20" viewBox="0 0 20 20"><circle cx="10" cy="10" r="9" fill="none" stroke="#ffe4d6"/><path d="M6 10l3 3 5-6" fill="none" stroke="#ffe4d6"/></svg><span>Trusted<br>Competent</span></div>
  <div class="why-item" style="left:402px"><svg width="20" height="20" viewBox="0 0 20 20"><circle cx="10" cy="10" r="9" fill="none" stroke="#ffe4d6"/><path d="M6 10l3 3 5-6" fill="none" stroke="#ffe4d6"/></svg><span>Dedication<br>Customizable</span></div>
  <div class="why-item" style="left:614px"><svg width="20" height="20" viewBox="0 0 20 20"><circle cx="10" cy="10" r="9" fill="none" stroke="#ffe4d6"/><path d="M6 10l3 3 5-6" fill="none" stroke="#ffe4d6"/></svg><span>Clear Price<br>Compliant</span></div>
  <div class="why-item" style="left:801px"><svg width="20" height="20" viewBox="0 0 20 20"><circle cx="10" cy="10" r="9" fill="none" stroke="#ffe4d6"/><path d="M6 10l3 3 5-6" fill="none" stroke="#ffe4d6"/></svg><span>Infrastructure<br>Man Power</span></div>
</section>

<section class="news">
  <h2 class="section-title" style="top:70px">LATEST NEWS</h2>
  <div class="section-tag" style="top:118px">BLOG AREA</div>

  <article class="news-card" style="left:232px">
    <div class="news-photo" role="img" aria-label="Photo of a person working on a laptop outdoors" style="background:linear-gradient(160deg,#c9ccc8,#e9e6e2 55%,#8c8a86)"><span class="news-badge">LATEST NEWS 1</span></div>
    <div class="news-body">
      <div class="news-meta">By Admin &nbsp;|&nbsp; Mar 21, 2019</div>
      <h3 class="news-title">Lacinia eget consecte sed convallis.</h3>
      <p class="news-text">Quasi architebeatae vitae dicta sunt explicabo nemo enim ipsam volupatem quia voluptassit asper natur aut ...</p>
      <div class="news-more">Continue Reading ⟶</div>
    </div>
  </article>

  <article class="news-card" style="left:482px">
    <div class="news-photo" role="img" aria-label="Photo of a gloved hand placing a sample under a microscope" style="background:linear-gradient(160deg,#b7bfc4,#e4e6e8 55%,#23313a)"><span class="news-badge">LATEST NEWS 1</span></div>
    <div class="news-body">
      <div class="news-meta">By Admin &nbsp;|&nbsp; Mar 21, 2019</div>
      <h3 class="news-title">Haematopoietic stem cell transplant.</h3>
      <p class="news-text">Quasi architebeatae vitae dicta sunt explicabo nemo enim ipsam volupatem quia voluptassit asper natur aut ...</p>
      <div class="news-more">Continue Reading ⟶</div>
    </div>
  </article>

  <article class="news-card" style="left:733px">
    <div class="news-photo" role="img" aria-label="Photo of a gloved hand placing a sample under a microscope" style="background:linear-gradient(160deg,#b7bfc4,#e4e6e8 55%,#23313a)"><span class="news-badge">LATEST NEWS 1</span></div>
    <div class="news-body">
      <div class="news-meta">By Admin &nbsp;|&nbsp; Mar 21, 2019</div>
      <h3 class="news-title">Excepteur sint occaecat cupidatat.</h3>
      <p class="news-text">Quasi architebeatae vitae dicta sunt explicabo nemo enim ipsam volupatem quia voluptassit asper natur aut ...</p>
      <div class="news-more">Continue Reading ⟶</div>
    </div>
  </article>
</section>

<footer class="site-footer">
  <div class="footer-brand">TrellanVita</div>
  <p class="footer-about">Lorem ipsum dolor amet constetur adipisicing elit sed eiusm tempor dunt labore dolore magna aliqua enim ad minim veniam.</p>
  <div class="socials"><span></span><span></span><span></span><span></span></div>

  <div class="footer-col" style="left:419px">
    <h4>Quick Link</h4>
    <ul class="footer-links"><li>Home</li><li>Research</li><li>Publications</li><li>Our Events</li><li>Future Team</li></ul>
  </div>

  <div class="footer-col" style="left:608px">
    <h4>Latest Posts</h4>
    <div style="margin-top:24px">
      <p class="post">Immunology: T-cell tweaks to target tumours.</p>
      <div class="post post-date"><svg width="12" height="12" viewBox="0 0 12 12"><rect x="1" y="2" width="10" height="9" fill="none" stroke="#d9d9de"/><path d="M1 5h10" stroke="#d9d9de"/></svg>Mar 28, 2019</div>
      <div class="post-divider"></div>
      <p class="post">Haematopoietic stem cell transplant.</p>
      <div class="post post-date"><svg width="12" height="12" viewBox="0 0 12 12"><rect x="1" y="2" width="10" height="9" fill="none" stroke="#d9d9de"/><path d="M1 5h10" stroke="#d9d9de"/></svg>Mar 28, 2019</div>
    </div>
  </div>

  <div class="footer-col" style="left:797px">
    <h4>NewsLetter</h4>
    <p class="post" style="margin-top:24px">Lorem ipsum dolor sit amet, consect etur adipisicing.</p>
    <div class="subscribe-input">Enter your email</div>
    <span class="btn subscribe-btn">Subscribe</span>
  </div>
</footer>
<div class="footer-bottom">© 2020, ALL RIGHTS RESERVED, <em>TRELLANVITA</em></div>

</div>
</body>
</html>
```